EPS Recycling Rpt

Our annual recycling rate report needs a tune up. Our organization helps faciltate expanded polystyrene (EPS) recycling and this 4-page report highlights growth trends and useful information to help readers understand the dynamics of EPS recycling. We need a designer that can recreate the brochure we've published over the past several years with some minor adjustments to accomodate new content.

A PDF of the 2012 report is attached. Header text should reflect 2013 in all cases. Please pay close attention to the new placement of the copy as indicated in the Word file (also attached) as it has been significantly modified from the 2012 version. The color pallette for our branding is provided. Contact us with any questions.

```html
<!DOCTYPE html>
<html lang="en">
<head>
<meta charset="utf-8">
<title>2013 EPS Recycling Rate Report</title>
<link href="https://fonts.googleapis.com/css2?family=Open+Sans:wght@300;400;600;700&display=swap" rel="stylesheet">
<style>
  :root {
    --green: #8cb43c;
    --green-dark: #6f9a2a;
    --blue: #1e8fc6;
    --orange: #f08a1c;
    --text: #5a5a5a;
    --paper: #ffffff;
  }
  * { margin: 0; padding: 0; box-sizing: border-box; }
  html, body { width: 849px; height: 1200px; overflow: hidden; background: var(--paper); }
  body { font-family: "Open Sans", sans-serif; color: var(--text); position: relative; }

  .brand { position: absolute; left: 30px; top: 30px; width: 200px; font-size: 20px; font-weight: 600; color: var(--green-dark); line-height: 1.2; }

  .report-title { position: absolute; right: 34px; top: 26px; text-align: right; font-size: 30px; font-weight: 300; color: var(--orange); line-height: 36px; letter-spacing: 0.3px; }

  .copy { position: absolute; left: 285px; width: 530px; top: 150px; }
  .copy h2 { font-size: 13px; font-weight: 600; color: var(--green-dark); letter-spacing: 0.5px; margin-bottom: 10px; }
  .copy p { font-size: 11.6px; line-height: 17px; margin-bottom: 26px; }

  .features { position: absolute; left: 28px; top: 600px; width: 787px; display: flex; justify-content: space-between; }
  .feature { width: 233px; }
  .feature-photo { height: 172px; }
  .feature-label { height: 38px; margin-top: 8px; padding-left: 12px; font-size: 20px; font-weight: 700; color: #fff; line-height: 38px; letter-spacing: 0.5px; }
  .feature-body { height: 342px; margin-top: 6px; padding: 14px 14px; font-size: 12.6px; line-height: 20px; color: #fff; }

  .initiative .feature-label, .initiative .feature-body { background: var(--green); }
  .innovation .feature-label, .innovation .feature-body { background: var(--blue); }
  .fun .feature-label, .fun .feature-body { background: var(--orange); }

  .initiative .feature-photo { background: linear-gradient(160deg, #c9d7e4, #7f9a6a 70%, #5d6d52); }
  .innovation .feature-photo { background: linear-gradient(180deg, #e6e8e4, #9fb7c3 60%, #4a7c52); }
  .fun .feature-photo { background: linear-gradient(170deg, #9ec9e8, #d9c29a 65%, #6f8fa0); }
</style>
</head>
<body>
  <div class="brand">Foam Recovery Council</div>
  <h1 class="report-title">2013 EPS RECYCLING<br>RATE REPORT</h1>

  <section class="copy">
    <h2>RECYCLING CRITERIA</h2>
    <p>Not all materials are well suited for recycling. Post-consumer EPS packaging must be clean and free of tape, film and cardboard. Expanded polystyrene made with a fire retardant additive, typically used in the manufacture of EPS building insulation, requires special reprocessing conditions. To enhance collection efforts and maximize the investment in recycling equipment, FRC recycling locations concentrate on large volume, commercial sources of post-consumer EPS. Some locations also offer consumer drop-off access.</p>
    <h2>EPS COLLECTION &amp; REUSE</h2>
    <p>Expanded polystyrene (EPS) foam packaging is an excellent material for recycling and reuse with a 15 year history of environmental stewardship. Members of the Foam Recovery Council sponsor these efforts with ongoing financial support and active involvement in the collection and reprocessing of EPS. Recycling gives everybody a sense of well being. Working together with communities, local businesses and citizens, this unified approach is achieving increased awareness with bigger and better results – for a material often thought to be non-recyclable! Individually, none of these groups could have realized this exponential growth trend.</p>
  </section>

  <section class="features">
    <article class="feature initiative">
      <div class="feature-photo" role="img" aria-label="Volunteers in safety vests standing beside bags of collected foam"></div>
      <h3 class="feature-label">INITIATIVE</h3>
      <div class="feature-body">Northvale Chemicals in Monaca, Pennsylvania introduced a program for its employees to recycle their EPS foam. The initiative was so successful it spurred Northvale to take their recycling efforts further by partnering with the Keystone Resources Council (KRC) to collect EPS for recycling free of charge at KRC events that enabled hundreds of individuals to drop off over 1,300 cubic yards of unwanted EPS foam for recycling.</div>
    </article>
    <article class="feature innovation">
      <div class="feature-photo" role="img" aria-label="Tub and bottle of adhesive made from recycled foam"></div>
      <h3 class="feature-label">INNOVATION</h3>
      <div class="feature-body">While EPS is usually recycled into products such as coat hangers, insulation, decorative moldings and picture frames, new market developments continue to evolve. Ninefold Products launched a new recycled glue product, Glue, which is made from a blend of recycled polystyrene waste collected in the San Francisco Bay area and plant-based ingredients. This type of new and inventive market development is a key aspect of sustainable EPS recycling initiatives.</div>
    </article>
    <article class="feature fun">
      <div class="feature-photo" role="img" aria-label="Surfers on a beach holding boards made from recycled foam"></div>
      <h3 class="feature-label">FUN &amp; UNIQUE</h3>
      <div class="feature-body">For a fun and unique solution to EPS recycling, Foam-To-Fins collects material to make new surfboard blanks. With 18 collection sites in California, special events and corporate partnerships with Tidewater Outfitters, Swell Line and others, this initiative delivers a closed loop recycling solution and is spreading the word on surfing sustainability.</div>
    </article>
  </section>
</body>
</html>
```